Facial Cosmetic Business Card Design

I am a Physician certified in Serenox injections, Plumavel fillers,& Chemical Peels.
I do no surgery
I have 20 years experience in facial cosmetics
30+ years medical experience
name is not TM but thought something like "Luminara Visage" catches what I do and the look I get with minimal to no downtime and no recovery time.
I do home parties and also private home consultations and treatments in a relaxed atmosphere with no pressure.
Aestheology services upon referral to a private associate as well.
I have no logo, photo's or desigs so I am ope to suggestions
Updates

To all the MD is my medical degree

the MNGGC are my board certifications stands for Member National Guild General Care
4816 Tallow Brook Lane is my office home address
5552148390 is my cell/office number or contact info

Thanks

Reason: Sorry was out of town I like a few of the designs so I have enough to choose from set tweeks to be done with prof degree and address mixup. Once i see corrections I will choose approp one thanks all Dr Halvorsen

Target Market(s)

mostly wome do these procedures usually i the above 35 crowd certainly over 40 crowd for sure

Industry/Entity Type

Medical

Contact Information for Business Card

Luminara Visage, Gregory Halvorsen MD, MNGGC
4816 Tallow Brook Lane
Fairhollow, Ga. 30099
O:555-218-4471
C:555-214-8390
F:555-218-4479

```html
<!DOCTYPE html>
<html lang="en">
<head>
<meta charset="utf-8">
<title>Luminara Visage – Gregory Halvorsen MD MNGGC</title>
<link rel="stylesheet" href="https://fonts.googleapis.com/css2?family=Pinyon+Script&family=Open+Sans:wght@400&display=swap">
<style>
  :root {
    --card-bg: #ffffff;
    --card-edge: #c9c9c9;
    --ink: #111111;
    --text-soft: #222222;
    --bronze: #8a5a2e;
    --bronze-soft: #a0703f;
    --portrait-light: #f6f3f1;
    --portrait-mid: #e9e2dd;
  }
  * { margin: 0; padding: 0; box-sizing: border-box; }
  html, body {
    width: 1200px;
    height: 693px;
    overflow: hidden;
    background: var(--card-bg);
  }
  .card {
    position: relative;
    width: 1200px;
    height: 693px;
    background: var(--card-bg);
    border: 2px solid var(--card-edge);
    font-family: "Open Sans", "Segoe UI", sans-serif;
    color: var(--ink);
  }
  .brand-name {
    position: absolute;
    left: 205px;
    top: 10px;
    font-family: "Pinyon Script", cursive;
    font-size: 150px;
    line-height: 1.2;
    font-weight: 400;
    color: var(--bronze);
    white-space: nowrap;
  }
  .portrait-art {
    position: absolute;
    left: 40px;
    top: 205px;
    width: 335px;
    height: 385px;
    border-radius: 50% 45% 40% 50% / 40% 40% 55% 55%;
    background: radial-gradient(ellipse at 55% 45%, var(--portrait-light) 0%, var(--portrait-mid) 100%);
  }
  .practitioner {
    position: absolute;
    right: 195px;
    top: 355px;
    text-align: right;
  }
  .practitioner-name {
    font-size: 58px;
    font-weight: 400;
    line-height: 1.1;
    letter-spacing: 0.5px;
    color: var(--ink);
  }
  .credentials {
    margin-top: 4px;
    font-size: 29px;
    letter-spacing: 2px;
    color: var(--bronze-soft);
  }
  .contact {
    position: absolute;
    right: 68px;
    bottom: 40px;
    text-align: right;
    font-style: normal;
    font-size: 27px;
    color: var(--text-soft);
  }
  .address { line-height: 1.5; }
  .phones {
    display: flex;
    justify-content: flex-end;
    gap: 22px;
    line-height: 1.4;
  }
  .phone-item {
    display: inline-flex;
    align-items: center;
    gap: 8px;
  }
  .phone-icon {
    width: 26px;
    height: 26px;
    fill: var(--bronze-soft);
  }
</style>
</head>
<body>
  <main class="card">
    <h1 class="brand-name">Luminara Visage</h1>

    <div class="portrait-art" role="img" aria-label="Line illustration of a woman's profile with red lips"></div>

    <section class="practitioner">
      <h2 class="practitioner-name">Gregory Halvorsen</h2>
      <p class="credentials">MD MNGGC</p>
    </section>

    <address class="contact">
      <p class="address">4816 Tallow Brook Lane Fairhollow, Ga. 30099</p>
      <p class="phones">
        <span class="phone-item">
          <svg class="phone-icon" viewBox="0 0 24 24" aria-label="Office">
            <path d="M6.6 10.8a15.1 15.1 0 0 0 6.6 6.6l2.2-2.2c.3-.3.7-.4 1-.2 1.1.4 2.3.6 3.6.6.6 0 1 .4 1 1V20c0 .6-.4 1-1 1C10.6 21 3 13.4 3 4c0-.6.4-1 1-1h3.5c.6 0 1 .4 1 1 0 1.3.2 2.5.6 3.6.1.3 0 .7-.2 1z"/>
          </svg>555-218-4471
        </span>
        <span class="phone-item">
          <svg class="phone-icon" viewBox="0 0 24 24" aria-label="Cell">
            <path d="M7 1h10a2 2 0 0 1 2 2v18a2 2 0 0 1-2 2H7a2 2 0 0 1-2-2V3a2 2 0 0 1 2-2zm0 3v14h10V4zm5 15.5a1.2 1.2 0 1 0 0 2.4 1.2 1.2 0 0 0 0-2.4z"/>
          </svg>555-214-8390
        </span>
        <span class="phone-item">
          <svg class="phone-icon" viewBox="0 0 24 24" aria-label="Fax">
            <path d="M7 2h8l3 3v5h1a3 3 0 0 1 3 3v8H2v-8a3 3 0 0 1 3-3h2zm2 2v6h7V6h-2V4zM5 14v2h3v-2zm5 0v2h3v-2zm5 0v2h3v-2zM5 17.5v1.5h3v-1.5zm5 0v1.5h3v-1.5zm5 0v1.5h3v-1.5z"/>
          </svg>555-218-4479
        </span>
      </p>
    </address>
  </main>
</body>
</html>
```